Grey orchard secret

UPDATED BRIEF:
I'm just updating the brief to enable any new submissions to come up with their own ideas. I have tried to offer my ideas below, but I am too close to the project therefor any new submissions are probably best using your talent. The main thing is it stands out and someone would want to buy it against the competition. All submissions have been excellent, so to be fair I will put the winning vote to family and friends. I am too close and biased to make the final choice.
This book is part memoire/ part biography/ part diary/ part self help.
My world is falling apart. I use the analogy of being lost at see. This book is my ships log. It could be a torn out PAGE of the log, a POSTER, or A MESSAGE a bottle.
It needs to be clear in the title, so GREY ORCHARD SECRET needs to stand out. BOO could be a wax seal, like a stamp. 'You've found the' and 'We're dancing at dusk' are less important. The title is: BOO You've found the GREY ORCHARD SECRET We're dancing at dusk.
Other subliminal random words are: family, paranoia, sex addiction, depression, marriage, divorce.
The other idea is flame red. Needs to be subtle to show my life is going up in flames. The diary page/poster/note should be singed or worn.
Ideally text font should be bespoke. Whether some or all are slightly wonky to show that my life is falling apart.
Octopus bottom left with tentacles spread over spine is a firm favourite
Text on spine needs to be large to stand out. Open to suggestions but nothing over simple.Good luck

Target Market(s)

30-60 years

Colors

Requirements
Must have
• Book size. I'm assuming: 21.5cm x 13.5cm x 2.5cm. I will need ebook version and paperback version. ISBN details will follow later

```html
<!DOCTYPE html>
<html lang="en">
<head>
<meta charset="utf-8">
<title>BOO You've found the GREY ORCHARD SECRET – book cover</title>
<link rel="stylesheet" href="https://fonts.googleapis.com/css2?family=Bebas+Neue&family=Montserrat:wght@400;700&family=Oswald:wght@600&family=Caveat+Brush&family=Reenie+Beanie&display=swap">
<style>
  :root {
    --flame: #c9161b;
    --flame-deep: #7a0a0c;
    --ember: #e0392a;
    --ink: #1a1a1a;
    --paper: #f0ebe1;
    --grid: #c9cfd6;
    --pencil: #8a8a90;
    --white: #ffffff;
  }
  * { margin: 0; padding: 0; box-sizing: border-box; }
  html, body { width: 1200px; height: 846px; overflow: hidden; background: var(--flame-deep); }

  .cover {
    position: relative;
    width: 1200px; height: 846px;
    background:
      radial-gradient(ellipse 60% 55% at 75% 45%, rgba(240,60,40,0.35), transparent 70%),
      radial-gradient(ellipse 50% 50% at 22% 35%, rgba(230,40,35,0.25), transparent 70%),
      radial-gradient(ellipse 120% 110% at 50% 50%, var(--flame) 45%, var(--flame-deep) 100%);
    overflow: hidden;
  }

  /* ---------- back cover ---------- */
  .back-blurb {
    position: absolute;
    left: 50px; top: 74px; width: 472px;
    color: var(--white);
    font-family: "Montserrat", sans-serif;
    font-weight: 700;
    font-size: 12.2px;
    line-height: 18.6px;
    text-align: justify;
  }
  .back-blurb p + p { margin-top: 18px; }
  .back-blurb .topics { text-align: left; }

  .back-creature {
    position: absolute;
    left: -60px; top: 420px; width: 600px; height: 480px;
    border-radius: 48% 52% 40% 45%;
    background: radial-gradient(ellipse at 35% 40%, #3a0507 0%, #5a0708 45%, rgba(122,10,12,0) 72%);
  }

  /* ---------- spine ---------- */
  .spine {
    position: absolute;
    left: 546px; top: 0; width: 108px; height: 846px;
  }
  .spine-title {
    position: absolute;
    top: 40px; left: 14px; height: 540px;
    writing-mode: vertical-rl;
    color: var(--white);
    display: flex; flex-direction: column;
  }
  .spine-title .main {
    font-family: "Bebas Neue", sans-serif;
    font-size: 33px; letter-spacing: 0.5px; line-height: 40px;
  }
  .spine-title .sub {
    font-family: "Caveat Brush", cursive;
    font-size: 27px; line-height: 34px;
  }
  .spine-author {
    position: absolute;
    left: 34px; top: 600px; width: 42px; height: 246px;
    background: var(--ink);
    color: var(--white);
    writing-mode: vertical-rl;
    font-family: "Montserrat", sans-serif;
    font-size: 19px; letter-spacing: 3px;
    display: flex; align-items: center; justify-content: flex-start;
    padding-top: 16px;
  }

  /* ---------- front cover ---------- */
  .tagline {
    position: absolute;
    left: 654px; width: 546px; top: 28px;
    text-align: center;
    color: var(--white);
    font-family: "Oswald", sans-serif;
    font-weight: 600; font-size: 25px; letter-spacing: 0.5px;
  }

  .log-page {
    position: absolute;
    left: 696px; top: 66px; width: 350px; height: 572px;
    background-color: var(--paper);
    background-image:
      linear-gradient(var(--grid) 1px, transparent 1px),
      linear-gradient(90deg, var(--grid) 1px, transparent 1px);
    background-size: 14px 14px;
    background-position: 6px 30px;
    box-shadow: 0 4px 14px rgba(60,0,0,0.45), inset 0 0 40px rgba(150,110,70,0.25);
  }
  .torn-edge { position: absolute; right: -10px; top: 0; width: 22px; height: 100%; }

  .pin {
    position: absolute; left: 165px; top: 18px;
    width: 18px; height: 18px; border-radius: 50%;
    background: radial-gradient(circle at 35% 35%, #fafafa, #8d8d8d 60%, #4a4a4a);
    box-shadow: 1px 2px 3px rgba(0,0,0,0.45);
  }

  .note-word {
    position: absolute;
    font-family: "Reenie Beanie", cursive;
    color: var(--pencil);
    line-height: 1;
  }
  .note-word.paranoia { left: 22px; top: 48px; font-size: 26px; transform: rotate(-4deg); }
  .note-word.addiction { left: 24px; top: 120px; font-size: 24px; transform: rotate(-6deg); width: 80px; }
  .note-word.family { left: 246px; top: 118px; font-size: 40px; transform: rotate(-20deg); }

  .title-block { position: absolute; left: 0; top: 150px; width: 350px; text-align: center; color: var(--ink); }
  .title-seal {
    display: block;
    font-family: "Bebas Neue", sans-serif;
    font-size: 92px; line-height: 0.9;
    transform: translateX(28px);
  }
  .title-lead {
    display: block;
    font-family: "Caveat Brush", cursive;
    font-size: 37px; line-height: 1;
    margin-top: 4px;
  }
  .title-main {
    display: block;
    font-family: "Bebas Neue", sans-serif;
    line-height: 0.92;
    margin-top: 10px;
  }
  .title-main .line1 { display: block; font-size: 68px; }
  .title-main .line2 { display: block; font-size: 96px; }
  .title-tail {
    display: block;
    font-family: "Caveat Brush", cursive;
    font-size: 37px; line-height: 1.05;
    margin-top: 8px;
  }

  .front-creature {
    position: absolute;
    left: 640px; top: 618px; width: 350px; height: 200px;
    border-radius: 50% 50% 45% 45%;
    background: radial-gradient(ellipse at 45% 45%, #111 0%, #1e1e1e 50%, rgba(26,26,26,0) 74%);
  }

  .front-author {
    position: absolute;
    left: 654px; width: 546px; top: 812px;
    text-align: center;
    color: var(--white);
    font-family: "Montserrat", sans-serif;
    font-size: 23px; letter-spacing: 2px;
  }
</style>
</head>
<body>
<main class="cover">

  <section class="back">
    <div class="back-creature" role="img" aria-label="Illustration of a large dark red octopus with tentacles spread towards the spine"></div>
    <div class="back-blurb">
      <p>So, you've found your career, got married, bought your home. Life is great, you are happy, and everything just seems to fit into place. Then suddenly your perfect Utopia starts to fall apart. The life that was once full of promise, hope, and ambition, has gone. You've reached the summit and the panoramic view is not what you expected! The storm approaches and you panic. Worry, fear, and distress fill your mind. Congratulations you have reached the Nirvana of a: GOS!</p>
      <p>This book is an honest reflection of life according to a dreamer. Somebody who's lost his way. A person who has it all, yet, has nothing. Who has lost his place in society, has so much to give, yet feels so empty and hopeless . A story of living life with depression. The highs and lows of a family man just trying to make it in life. The ultimate guide to a fragile mind in Grey orchard secret fighting:</p>
      <p class="topics">Sex addiction, Periods, the menopause, Marriage conflict, Parenting, finance, family, Divorce, and Affairs</p>
    </div>
  </section>

  <section class="spine">
    <div class="spine-title">
      <span class="main">BOO YOU'VE FOUND THE GREY ORCHARD SECRET</span>
      <span class="sub">We're dancing at dusk</span>
    </div>
    <div class="spine-author">MARTIN HALE</div>
  </section>

  <section class="front">
    <p class="tagline">THE NUMBER ONE BESTDAD</p>

    <div class="log-page">
      <svg class="torn-edge" viewBox="0 0 22 572" preserveAspectRatio="none" aria-hidden="true">
        <path d="M0 0 L22 0 L14 8 L22 16 L14 24 L22 32 L14 40 L22 48 L14 56 L22 64 L14 72 L22 80 L14 88 L22 96 L14 104 L22 112 L14 120 L22 128 L14 136 L22 144 L14 152 L22 160 L14 168 L22 176 L14 184 L22 192 L14 200 L22 208 L14 216 L22 224 L14 232 L22 240 L14 248 L22 256 L14 264 L22 272 L14 280 L22 288 L14 296 L22 304 L14 312 L22 320 L14 328 L22 336 L14 344 L22 352 L14 360 L22 368 L14 376 L22 384 L14 392 L22 400 L14 408 L22 416 L14 424 L22 432 L14 440 L22 448 L14 456 L22 464 L14 472 L22 480 L14 488 L22 496 L14 504 L22 512 L14 520 L22 528 L14 536 L22 544 L14 552 L22 560 L14 572 L0 572 Z" fill="#d63a2c"/>
        <line x1="9" y1="0" x2="9" y2="572" stroke="#f0ebe1" stroke-width="2" stroke-dasharray="4 6"/>
      </svg>
      <span class="pin"></span>
      <span class="note-word paranoia">Paranoia</span>
      <span class="note-word addiction">SEX addiction</span>
      <span class="note-word family">FAMILY</span>

      <h1 class="title-block">
        <span class="title-seal">BOO</span>
        <span class="title-lead">You've found the</span>
        <span class="title-main"><span class="line1">GREY ORCHARD</span><span class="line2">SECRET</span></span>
        <span class="title-tail">We're dancing<br>at dusk</span>
      </h1>
    </div>

    <div class="front-creature" role="img" aria-label="Illustration of a black octopus with a yellow eye curling its tentacles beneath the log page"></div>
    <p class="front-author">MARTIN HALE</p>
  </section>

</main>
</body>
</html>
```